Business card design for web travel company

Hi
we'd like to receive some proposal for a business card design.
Stayvano is a private travel club, dedicated to all travel lovers, with unique offers for exclusive destinations all around the world. At Stayvano you can find a wide range of offers for resorts, boutique hotels and travel packages at the best guaranteed price available on the market. The convenience of the offer is guaranteed by a private sales model: offers are available for a limited time only and they are personally chosen by Stayvano's qualified team of travel experts.
We offer only exclusive hotels with discounted prices but we are not an outlet or a discount supermarket: the design should reflect our connection with luxury, exclusivity using the same style of our website www.stayvano-example.com.
We want to make sure that when we'll present ourself to our business partner they will feel immediately which is our brand positioning giving them also a sense of an affordable and reliable partner.
In attachment you can also find our brand guidelines (please note that we are NOT USING ANY MORE THE TAG LINE "Five star outlet" mentioned in it).
The info to be inserted are:
Name Surname
Job Title
Tel
Mobile (when needed)
Email
Stayvano S.r.l.
Via Bruno Lesta 27
20131 Milano

```html
<!DOCTYPE html>
<html lang="en">
<head>
<meta charset="utf-8">
<title>Stayvano — Business Card</title>
<link href="https://fonts.googleapis.com/css2?family=Questrial&display=swap" rel="stylesheet">
<style>
  :root {
    --ink-black: #050505;
    --night: #1b1b1b;
    --gold: #c2b07a;
    --silver: #c9c9c9;
    --name-grey: #b9b9b9;
    --text-light: #dcdcdc;
    --logo-ink: #1e1e1e;
    --stone-light: #b8b8b8;
    --stone-dark: #3e3e3e;
  }
  html, body {
    margin: 0;
    padding: 0;
    width: 1200px;
    height: 721px;
    overflow: hidden;
    background: #fff;
  }
  .card {
    position: relative;
    width: 1200px;
    height: 721px;
    overflow: hidden;
    font-family: "Questrial", "Century Gothic", sans-serif;
  }
  .card__top {
    position: absolute;
    left: 0; top: 0;
    width: 1200px; height: 464px;
    background:
      radial-gradient(ellipse 320px 420px at 690px 330px, rgba(70,70,70,0.55), rgba(0,0,0,0) 70%),
      linear-gradient(90deg, var(--ink-black) 0%, var(--night) 45%, var(--night) 65%, var(--ink-black) 100%);
  }
  .card__rule {
    position: absolute;
    left: 0; top: 464px;
    width: 1200px; height: 8px;
    background: var(--gold);
  }
  .card__bottom {
    position: absolute;
    left: 0; top: 472px;
    width: 1200px; height: 249px;
    background:
      radial-gradient(ellipse 620px 330px at 300px 721px, var(--stone-light) 0%, #8a8a8a 50%, var(--stone-dark) 100%);
  }
  .contact {
    position: absolute;
    right: 177px;
    top: 0;
    text-align: right;
  }
  .contact__name {
    position: absolute;
    right: 0; top: 112px;
    margin: 0;
    font-size: 58px;
    font-weight: 400;
    color: var(--name-grey);
    white-space: nowrap;
    letter-spacing: -0.5px;
  }
  .contact__title {
    position: absolute;
    right: -2px; top: 178px;
    font-size: 32px;
    letter-spacing: 6px;
    color: var(--gold);
    white-space: nowrap;
  }
  .contact__row {
    position: absolute;
    right: 0;
    display: flex;
    align-items: center;
    gap: 34px;
    white-space: nowrap;
  }
  .contact__value {
    font-size: 24px;
    letter-spacing: 2.4px;
    color: var(--text-light);
  }
  .contact__icon { width: 28px; height: 26px; display: block; }
  .contact__row--tel { top: 228px; }
  .contact__row--mobile { top: 276px; }
  .contact__row--email { top: 323px; }
  .contact__address {
    position: absolute;
    right: 0; top: 374px;
    font-size: 19px;
    line-height: 17.5px;
    letter-spacing: 0.5px;
    color: var(--text-light);
    white-space: nowrap;
  }
  .brand {
    position: absolute;
    left: 86px; top: 495px;
    font-size: 84px;
    letter-spacing: 1px;
    color: var(--logo-ink);
    line-height: 1;
  }
</style>
</head>
<body>
<main class="card">
  <div class="card__top"></div>
  <div class="card__rule"></div>
  <div class="card__bottom"></div>

  <section class="contact">
    <h1 class="contact__name">JOHN DOE</h1>
    <div class="contact__title">Job Title</div>

    <div class="contact__row contact__row--tel">
      <span class="contact__value">00 123 4567 890</span>
      <svg class="contact__icon" viewBox="0 0 28 26" aria-label="Telephone">
        <path fill="var(--gold)" d="M2 9c0-4 4-6 12-6s12 2 12 6v2h-6V8c-2-1-10-1-12 0v3H2z"/>
        <path fill="var(--gold)" d="M6 12h16l4 12H2z"/>
        <circle cx="14" cy="18" r="3.2" fill="var(--ink-black)"/>
      </svg>
    </div>

    <div class="contact__row contact__row--mobile">
      <span class="contact__value">00 123 4567 890</span>
      <svg class="contact__icon" viewBox="0 0 28 26" aria-label="Mobile">
        <rect x="4" y="3" width="20" height="22" rx="2" fill="var(--gold)"/>
        <rect x="7" y="6" width="14" height="5" fill="var(--ink-black)"/>
        <g fill="var(--ink-black)">
          <rect x="7" y="13" width="3" height="2.5"/><rect x="12.5" y="13" width="3" height="2.5"/><rect x="18" y="13" width="3" height="2.5"/>
          <rect x="7" y="17" width="3" height="2.5"/><rect x="12.5" y="17" width="3" height="2.5"/><rect x="18" y="17" width="3" height="2.5"/>
          <rect x="7" y="21" width="3" height="2.5"/><rect x="12.5" y="21" width="3" height="2.5"/><rect x="18" y="21" width="3" height="2.5"/>
        </g>
        <rect x="18" y="0" width="3" height="4" fill="var(--gold)"/>
      </svg>
    </div>

    <div class="contact__row contact__row--email">
      <span class="contact__value">johndoe@stayvano-example.com</span>
      <svg class="contact__icon" viewBox="0 0 28 26" aria-label="Email">
        <path fill="var(--gold)" d="M1 11L14 2l13 9v13H1z"/>
        <path fill="none" stroke="var(--ink-black)" stroke-width="1.6" d="M1 11l13 8 13-8M1 24l10-8M27 24l-10-8"/>
      </svg>
    </div>

    <address class="contact__address" style="font-style:normal">
      Stayvano S.r.l.<br>
      Via Bruno Lesta 27<br>
      20131 Milano
    </address>
  </section>

  <div class="brand">Stayvano</div>
</main>
</body>
</html>
```